Need a Revamped Website - WaveCrestline.com

I am looking for a website designed for www.wavecrestline.com
The present website has content relating to the Kabwe Airwave Gathering - an annual meeting for radio practitioners in Zambia. My intention is to change the focus: to make the website a resource hub for radio practitioners in Africa. The site is to have the following:
Featured articles (opinion pieces) contributed by industry insiders.
Links to various radio stations websites
An events calendar focusing on radio related events
News (radio industry updates) etc
The site should also be able to incorporate social media mechanisms such as 'Likes' through to Circlewall or articles to be shared on Birdcall etc.
The focus of the word Summit, for the purposes of the website, should shift. Instead of the meaning "meeting/ convention", it'll shift to connote "height, pinnacle (of radio excellence)".
The design should have a modern, contemporary feel.
Target Market(s)
The main target audience is radio deejays, radio station management, marketers/ advertisers, journalists.

```html
<!DOCTYPE html>
<html lang="en">
<head>
<meta charset="utf-8">
<title>WaveCrestline</title>
<link href="https://fonts.googleapis.com/css2?family=Sorts+Mill+Goudy&display=swap" rel="stylesheet">
<style>
:root{
  --black:#0b0b0b;
  --panel:#0d0d0d;
  --white:#ffffff;
  --orange:#f57a1f;
  --splash:#3b3bf6;
  --grey-top:#ffffff;
  --grey-bottom:#a9a9a9;
  --like-border:#9aa8c6;
  --like-text:#3b5b99;
}
*{margin:0;padding:0;box-sizing:border-box}
html,body{width:1200px;height:1176px;overflow:hidden;background:var(--black)}
body{position:relative;font-family:"Sorts Mill Goudy",Georgia,serif;color:var(--white)}
.page{position:absolute;left:10px;top:0;width:1183px;height:1000px;background:var(--white)}
.splash{position:absolute;left:0;top:140px;width:1183px;height:860px;
  background:radial-gradient(ellipse 55% 50% at 45% 50%,var(--splash) 0%,var(--splash) 60%,rgba(59,59,246,.35) 80%,rgba(59,59,246,0) 100%)}
.header{position:absolute;left:58px;top:12px;width:1118px;height:113px;border-radius:12px;
  background:linear-gradient(#0a0a0a,#1c1c1c 70%,#050505)}
.brand{position:absolute;left:34px;top:10px;font-size:42px;color:var(--orange);letter-spacing:1px}
.nav{position:absolute;left:4px;top:78px;width:1106px;height:33px;border-radius:10px;
  background:linear-gradient(#2a2a2a,#0a0a0a);display:flex;padding-left:71px}
.nav a{color:var(--white);text-decoration:none;font-size:24px;line-height:33px;margin-right:41px;white-space:nowrap}
.search{position:absolute;left:898px;top:174px;display:flex;align-items:center;color:var(--black);font-size:24px}
.search span{margin-right:7px}
.search .field{width:150px;height:30px;border:2px solid var(--black);background:var(--white)}
.featured{position:absolute;left:58px;top:262px;width:808px;height:486px;background:var(--panel);border-radius:8px}
.featured h2{position:absolute;left:29px;top:8px;font-weight:normal;font-size:25px}
.accent{color:var(--orange)}
.article{position:absolute;font-size:19px;line-height:21.5px}
.like{position:absolute;display:flex;align-items:center;gap:5px;height:30px;padding:0 8px;
  background:linear-gradient(#ffffff,#e6e9f0);border:2px solid var(--like-border);border-radius:2px;
  color:var(--like-text);font-family:Arial,sans-serif;font-size:14px}
.like i{display:block;width:13px;height:12px;border:2px solid var(--like-text);border-radius:2px}
.calendar{position:absolute;left:882px;top:262px;width:308px;height:488px;
  background:linear-gradient(#1a1a0a 0%,#6b7a1a 18%,#101010 40%,#0a0a0a 100%)}
.updates-tab{position:absolute;left:62px;top:775px;height:26px;padding:0 8px;background:var(--black);
  border-radius:8px 8px 0 0;color:var(--orange);font-size:24px;line-height:26px}
.updates{position:absolute;left:62px;top:796px;width:766px;height:181px;background:var(--black);border-radius:8px}
.updates .inner{position:absolute;left:8px;top:4px;width:748px;height:172px;border-radius:8px;
  background:linear-gradient(var(--grey-top),var(--grey-bottom))}
.update{position:absolute;color:var(--black);font-size:14.5px;line-height:16.7px}
.footer{position:absolute;left:0;top:1000px;width:1200px;height:176px}
.partner{position:absolute;top:21px;width:146px;height:104px;background:#f4f4f4}
.social{position:absolute;left:840px;width:298px;text-align:right;white-space:nowrap;font-size:17px}
.social-mark{position:absolute;left:1146px;width:48px;height:48px;border-radius:8px;background:#3b6aa8}
.footer-nav{position:absolute;left:442px;top:1150px;font-size:15px;display:flex;gap:10px}
.footer-nav a{color:var(--white);text-decoration:none}
</style>
</head>
<body>
<div class="page">
  <div class="splash" role="img" aria-label="Blue paint splatter behind the content"></div>
</div>

<header class="header">
  <div class="brand">WaveCrestline</div>
  <nav class="nav">
    <a href="#">Home</a><a href="#">About</a><a href="#">Speakers</a><a href="#">Gallery</a><a href="#">Partners</a><a href="#">Contact</a>
  </nav>
</header>

<div class="search"><span>Search</span><div class="field"></div></div>

<section class="featured">
  <h2><span class="accent">Featured</span> articles</h2>
  <p class="article" style="left:29px;top:95px;width:720px">Got a radio show coming up, tell us about it here. DJs, Promoters and Producers this sec-tion is for you.</p>
  <div class="like" style="left:690px;top:134px"><i></i>Like</div>
  <p class="article" style="left:29px;top:213px;width:778px">The world in the music industry has a lot of issues and events that trigger critiques to give their opinions and views regarding a certain subject. These views are either constructive or destructive to the enthusiasts in the music world.</p>
  <div class="like" style="left:693px;top:280px"><i></i>Like</div>
  <p class="article" style="left:24px;top:354px;width:780px">The biggest advantage of downloading music from sites that offer music legally is that you are assured that the music is of a good quality and you can also be rest assured that by downloading the music onto your mp3 you are not breaking any laws. This is the reason why most of the expe-rienced and dedicated music lovers all over the world get their music only after research.</p>
  <div class="like" style="left:693px;top:448px"><i></i>Like</div>
</section>

<aside class="calendar" role="img" aria-label="2011 events calendar poster with glowing equaliser lights"></aside>

<div class="updates-tab">Latest updates</div>
<section class="updates">
  <div class="inner">
    <p class="update" style="left:23px;top:16px;width:240px">The Velvet Harbour Choir have recorded a world-exclusive track for Northgate Radio West which will air<br>during their Westland Music Day today (Friday).</p>
    <div class="like" style="left:258px;top:114px"><i></i>Like</div>
    <p class="update" style="left:398px;top:16px;width:236px">Groove FM has signed a sponsorship deal with Aerolis to launch a new travel show, Groove Journeys.The pro-gramme will be hosted by Nadia Cole and broadcast every Tuesday from 6-7pm, and feature special guests including chicago-born jazz singer Marcus Dell in the first edition</p>
    <div class="like" style="left:656px;top:120px"><i></i>Like</div>
  </div>
</section>

<footer class="footer">
  <div class="partner" style="left:93px" role="img" aria-label="Partner badge"></div>
  <div class="partner" style="left:287px" role="img" aria-label="Partner badge"></div>
  <div class="partner" style="left:483px;background:#5aa33a" role="img" aria-label="Partner badge"></div>
  <div class="partner" style="left:683px" role="img" aria-label="Partner badge"></div>
  <div class="social" style="top:39px">Follow WaveCrestline on Birdcall</div>
  <div class="social-mark" style="top:27px;background:#4fb6e3"></div>
  <div class="social" style="top:94px">Friend WaveCrestline on Circlewall</div>
  <div class="social-mark" style="top:80px"></div>
</footer>
<nav class="footer-nav">
  <a href="#">Home</a><a href="#">About</a><a href="#">Speakers</a><a href="#">Gallery</a><a href="#">Partners</a><a href="#">Contact</a>
</nav>
</body>
</html>
```